School Canteen Menu

We operate 30 school canteen/cafes across Melbourne. We are looking to update our old menu to a new attractive design.
We offer a variety of both food and drink and we need to highlight our healthy options. We would like to have a background picture of either salads or healthy sandwiche etc.
We have borken our current menu in catogories according to hot food, cold bar, drinks, ice creams etc.
We would prefer it to be a A4 design but other ideas are welcome.

In summary we need a vibrant attractive applealing design.
My business card with our lgo is also attached
Regards

Tam
Updates

We have two types of menu a secondary menu for students 12-18 and a primary school menu 5-12 year olds. I have attached samples of both.

Reason: Extended deadline as the director of business is away till sunday

Target Market(s)

12 year old to 18 year olds. School Students. As well as Teachers. Prehaps encouraging Teaches with our Freshly made salads will be a feature.

Industry/Entity Type

School

Requirements
Must have
• Viabrant Colors. Greens, Purples, Yellows.
Should not have
• Red Colors. Considered to be a unhealthy color.

```html
<!DOCTYPE html>
<html lang="en">
<head>
<meta charset="utf-8">
<title>Canteen Menu 2012</title>
<link rel="stylesheet" href="https://fonts.googleapis.com/css2?family=Ubuntu+Condensed&family=Carlito&family=Arimo&display=swap">
<style>
:root{
  --panel:rgba(250,250,246,0.78);
  --ink:#2a2a2a;
  --rule:#3a3a3a;
  --band:#1a1a1a;
  --band-text:#7cf21a;
  --bg-a:#a9c98a;
  --bg-b:#e9efe0;
  --bg-c:#6f9e55;
}
*{margin:0;padding:0;box-sizing:border-box}
html,body{width:1200px;height:1166px;overflow:hidden}
body{position:relative;font-family:"Ubuntu Condensed","Arial Narrow",sans-serif;color:var(--ink)}
.backdrop{position:absolute;inset:0;background:
  radial-gradient(circle at 10% 20%,#d8e8c8 0,transparent 35%),
  radial-gradient(circle at 85% 80%,#cfe3b6 0,transparent 40%),
  linear-gradient(135deg,var(--bg-a),var(--bg-b) 45%,var(--bg-c))}
.panel{position:absolute;left:47px;top:38px;width:1093px;height:1092px;background:var(--panel)}
.title{position:absolute;left:218px;top:58px;font-family:"Carlito",sans-serif;font-weight:400;font-size:40px;line-height:48px;color:#222}
.col{position:absolute}
.col h2{font-size:23px;font-weight:700;height:30px;line-height:30px;margin-left:8px}
.list{border-top:2px solid var(--rule)}
.row{display:flex;align-items:center;border-bottom:2px solid var(--rule);font-size:14px;line-height:22px;position:relative;white-space:nowrap}
.r1{height:25px}.r2{height:48px}.r3{height:70px}.r0{height:50px}
.name{padding-left:8px;white-space:nowrap}
.price{position:absolute}
.hot{left:60px;top:135px;width:298px}
.hot .price{left:240px}
.jaffle-label{position:absolute;left:22px;font-weight:700}
.jaffle{padding-left:86px}
.specials{left:60px;top:843px;width:298px}
.specials .price{left:240px}
.tight{font-size:13px;letter-spacing:-0.2px}
.bold{font-weight:700}
.plates{left:400px;top:135px;width:380px}
.plates .name{padding-left:130px}
.plates .price{left:323px}
.sub{display:block;padding-left:8px;font-size:13px;line-height:22px}
.sub b{font-size:14px}
.small{font-size:11px}
.note-in{position:absolute;left:207px;font-size:10.5px;line-height:14px;width:112px}
.sandwiches{left:400px;top:430px;width:380px}
.sandwiches .name{padding-left:130px}
.sandwiches .price{left:323px}
.wraps{left:400px;top:905px;width:380px}
.wraps .price{left:323px}
.wraps .kind{position:absolute;left:8px;width:110px;white-space:nowrap}
.wraps .fill{position:absolute;left:130px;width:190px;white-space:nowrap;font-size:13.5px}
.snacks{left:823px;top:135px;width:290px}
.drinks{left:823px;top:478px;width:290px}
.ices{left:823px;top:684px;width:290px}
.snacks .price,.drinks .price,.ices .price{left:233px}
.drinks .name{font-size:13.5px}
.legend{position:absolute;left:831px;top:945px;width:290px;font-size:13.5px;line-height:22px;white-space:nowrap}
.band{position:absolute;left:55px;top:1055px;width:1055px;height:45px;background:var(--band);color:var(--band-text);font-family:"Arimo",Arial,sans-serif;font-size:51px;line-height:45px;text-align:center;white-space:nowrap;overflow:hidden}
</style>
</head>
<body>
<div class="backdrop" role="img" aria-label="Background photo collage of fresh salads, fruit and healthy sandwiches"></div>
<div class="panel"></div>
<h1 class="title">Canteen Menu 2012</h1>

<section class="col hot">
  <h2>Hot Food</h2>
  <div class="list">
    <div class="row r1"><span class="jaffle-label">Jaffles</span><span class="name jaffle">Cheese</span><span class="price">$2.50</span></div>
    <div class="row r1"><span class="name jaffle">Spaghetti ☺</span><span class="price">$2.50</span></div>
    <div class="row r1"><span class="name jaffle">Baked Beans ☺</span><span class="price">$2.50</span></div>
    <div class="row r1"><span class="name jaffle">Ham &amp; Cheese</span><span class="price">$2.60</span></div>
    <div class="row r2"><span class="name jaffle">Ham, Cheese &amp;<br>Pineapple</span><span class="price">$3.00</span></div>
    <div class="row r1"><span class="name">Lasagne 97% Fat Free ☺</span><span class="price">$3.60</span></div>
    <div class="row r1"><span class="name tight">Macaroni &amp; Cheese 97% Fat Free ☺</span><span class="price">$3.60</span></div>
    <div class="row r1"><span class="name">Meat Pie</span><span class="price">$3.20</span></div>
    <div class="row r1"><span class="name">Party Pie or Party Sausage Roll</span><span class="price">$1.00</span></div>
    <div class="row r1"><span class="name">Sausage Roll</span><span class="price">$3.00</span></div>
    <div class="row r1"></div>
    <div class="row r2"><span class="name">Flame Grilled Beef Burger &nbsp;☺<br>with lettuce, cheese and tomato</span><span class="price">$4.00</span></div>
    <div class="row r0"><span class="name tight">Chicken Burger<br>with lettuce, cheese &amp; mayonnaise</span><span class="price">$4.00</span></div>
    <div class="row r3"><span class="name tight">Baked Chicken Schnitzel Roll<br>with lettuce, cheese, tomato &amp; mayo</span><span class="price">$4.20</span></div>
    <div class="row r1"><span class="name">Corn Cobette ☺</span><span class="price">$1.20</span></div>
    <div class="row r1"><span class="name">Noodles - Chicken or Beef</span><span class="price">$2.60</span></div>
    <div class="row r2"><span class="name">Chicken Nuggets 80c<br>each &nbsp;&nbsp;&nbsp;&nbsp;&nbsp;&nbsp;&nbsp;&nbsp;&nbsp;&nbsp;&nbsp;&nbsp;&nbsp;&nbsp;&nbsp;&nbsp;&nbsp;&nbsp;&nbsp;(3)</span><span class="price">$2.20</span></div>
    <div class="row r1"><span class="name">Steamed Dim Sim</span><span class="price">$0.90</span></div>
    <div class="row r1"><span class="name">Hot Dog</span><span class="price">$3.00</span></div>
    <div class="row r1"></div>
  </div>
</section>

<section class="col specials">
  <h2>Specials</h2>
  <div class="list">
    <div class="row r1"><span class="name bold">Health Pack 1</span><span class="price">$6.00</span></div>
    <div class="row r2"><span class="name">Salad Roll, Cookie &amp; 200ml Fruit Box<br>$5.00</span></div>
    <div class="row r1"><span class="name bold">Health Pack 2</span><span class="price">$6.00</span></div>
    <div class="row r2"><span class="name tight">Any 97% Fat Free Pasta,300ml FlavouredMilk<br>(FRESH)</span></div>
  </div>
</section>

<section class="col plates">
  <h2>Salad Plates</h2>
  <div class="list">
    <div class="row r0"><span class="sub"><b>Salad Plates</b><br><span class="small">all with lettuce, cucumber, carrot, tomato &amp; beetroot</span></span></div>
    <div class="row r1"><span class="name">Salad ☺</span><span class="price">$3.40</span></div>
    <div class="row r1"><span class="name">Egg ☺</span><span class="price">$3.60</span></div>
    <div class="row r2"><span class="name">Chicken ☺</span><span class="price">$3.90</span></div>
    <div class="row r1"><span class="name">Cheese</span><span class="price">$3.60</span></div>
    <div class="row r1"><span class="name">Ham ☺</span><span class="price">$3.60</span></div>
    <div class="row r1"><span class="name">Tuna ☺</span><span class="price">$3.60</span></div>
  </div>
</section>

<section class="col sandwiches">
  <h2>Sandwiches</h2>
  <div class="list" style="border-top:none">
    <div class="row r2"><span class="sub"><b>Sandwiches</b><br><b>Rolls</b> <span class="small">60c extra</span></span></div>
    <div class="row r2"><span class="name">Salad ☺</span><span class="note-in">lettuce, tomato, carrot,<br>beetroot, cucumber</span><span class="price">$2.80</span></div>
    <div class="row r1"><span class="name">Ham &amp; Tomato ☺</span><span class="price">$2.40</span></div>
    <div class="row r2"><span class="name">Ham, Cheese &amp; Tomato ☺</span><span class="price">$2.60</span></div>
    <div class="row r1"><span class="name">Cheese &amp; Tomato ☺</span><span class="price">$2.40</span></div>
    <div class="row r1"><span class="name">Cheese &amp; Salad ☺</span><span class="price">$3.00</span></div>
    <div class="row r2"><span class="name">Egg &amp; Lettuce ☺</span><span class="price">$2.80</span></div>
    <div class="row r1"><span class="name">Chicken &amp; Salad ☺</span><span class="price">$3.10</span></div>
    <div class="row r1"><span class="name">Tuna &amp; Tomato ☺</span><span class="price">$2.90</span></div>
    <div class="row r1"><span class="name tight">Tuna, Lettuce &amp; Mayonnaise</span><span class="price">$3.00</span></div>
    <div class="row r1"><span class="name">Veggie Spread</span><span class="price">$1.60</span></div>
    <div class="row r1"><span class="name">Ham</span><span class="price">$2.20</span></div>
    <div class="row r1"><span class="sub">extra fillings</span><span class="price">$0.40</span></div>
  </div>
</section>

<section class="col wraps">
  <h2>Wraps</h2>
  <div class="list" style="margin-top:18px">
    <div class="row r1"><span class="kind">BBQ Chicken</span><span class="fill">Chicken, Lettuce, BBQ Sauce</span><span class="price">$3.60</span></div>
    <div class="row r2"><span class="kind">Sweet Chilli<br>Chicken</span><span class="fill">Chicken, Lettuce, Sweet Chilli<br>Sauce</span><span class="price">$3.60</span></div>
  </div>
</section>

<section class="col snacks">
  <h2>Snacks</h2>
  <div class="list">
    <div class="row r1"><span class="name">Pikelets ☺</span><span class="price">$0.80</span></div>
    <div class="row r1"><span class="name">Pop Corn ☺</span><span class="price">$2.00</span></div>
    <div class="row r1"><span class="name">Fruit Salad – small ☺</span><span class="price">$1.50</span></div>
    <div class="row r1"><span class="name">Fruit of the day ☺</span><span class="price">$0.80</span></div>
    <div class="row r2"><span class="name">Jelly Cup with Fruit</span><span class="price">$1.50</span></div>
    <div class="row r1"><span class="name">Anzac Cookie</span><span class="price">$2.00</span></div>
    <div class="row r1"><span class="name">Mini Muffins (home baked)</span><span class="price">$0.80</span></div>
    <div class="row r1"></div>
    <div class="row r1"></div>
  </div>
</section>

<section class="col drinks">
  <h2>Drinks</h2>
  <div class="list">
    <div class="row r2"><span class="name">Flavoured Milk (3000ml) Chocolate,<br>Strawberry, Iced Coffee <b>(FRESH)</b></span><span class="price">$2.50</span></div>
    <div class="row r1"><span class="name">Water (600ml) ☺</span><span class="price">$2.30</span></div>
    <div class="row r2"><span class="name">Fruit Juice (200ml) Tropical, Orange,<br>Apple</span><span class="price">$1.5 0</span></div>
  </div>
</section>

<section class="col ices">
  <h2>Ice Creams</h2>
  <div class="list" style="margin-top:18px">
    <div class="row r1"><span class="name">Frozen Orange Wedge ☺</span><span class="price">$0.20</span></div>
    <div class="row r1"><span class="name">Frozen Pineapple Ring ☺</span><span class="price">$0.50</span></div>
    <div class="row r1"><span class="name">Frozen Fruit Yoghurt</span><span class="price">$2.00</span></div>
    <div class="row r1"><span class="name">Frosty Tube</span><span class="price">$0.80</span></div>
    <div class="row r1"><span class="name">Sun Cube_Orange, Lemonade</span><span class="price">$2.00</span></div>
    <div class="row r1"></div>
  </div>
</section>

<p class="legend">☺ Foods marked with a smiley are green foods<br>and can be eaten everyday</p>

<div class="band">Canteen Closed on Tuesdays &amp; Wednesdays</div>
</body>
</html>
```